Company Flyer for Electric boating company

I am looking for a company flyer which we can hand over to boat owners in the Netherlands (Amsterdam area). Our core business is to rebuild every boat (from 4 to 10 meters) into an electrically propelled boat. We are taking out diesels and replace them with a high quality electrical motor, inboard varying from 30 till 80 pk (hp). And outboard from 1pk (hp) till 200pk. We are the best, not the cheapest, not the most expensive. We only work with the best materials. The flyer has to be sort of in line with our website and branding.

Major advantages of electric boating are:
- completely silent
- no fumes, smells or smoke
- cheap to operate
- environmentally friendly
- obliged in more and more areas
- no maintenance
- more enjoyable

The flyer should be A5 format. Since all the text has to be in Dutch I expect only the graphical design and layout for advantages, process, pricing and contact details etc.

Target Market(s)

Boat owners in the Netherlands

Font styles to use
Sans Serif

Colors
9bcb3c
add136
cadf82
0555a3
3176b5
85acd3
e0ebf3

Requirements
Must have
• Clean design, in line with website: www.volta-kade.nl
Nice to have
• icons for advantages, boating etc

2 sides
Should not have
• Steering wheel...

```html
<!DOCTYPE html>
<html lang="en">
<head>
<meta charset="utf-8">
<title>Volta Kade – Electric Boating Flyer</title>
<link rel="stylesheet" href="https://fonts.googleapis.com/css2?family=Lato:wght@400;700;900&family=Michroma&display=swap">
<style>
  :root {
    --green: #7cb82f;
    --green-dark: #5f9421;
    --ink: #2b2c36;
    --text: #2f3033;
    --paper: #f5f5f3;
    --panel: #e8e8e6;
    --muted: #6d6e70;
    --black: #0c0c0d;
    --white: #ffffff;
  }
  * { box-sizing: border-box; margin: 0; padding: 0; }
  html, body {
    width: 900px; height: 1200px; overflow: hidden;
    background: var(--paper);
  }
  .flyer {
    position: relative; width: 900px; height: 1200px; overflow: hidden;
    background: var(--paper);
    font-family: "Lato", sans-serif; color: var(--text);
  }
  .hero-photo {
    position: absolute; left: 0; top: 0; width: 900px; height: 370px;
    background: linear-gradient(90deg, #15171d 0%, #2a2e36 22%, #c9ced3 45%, #eef0f2 52%, #c2c7cc 60%, #262a31 80%, #14161b 100%);
  }
  .headline {
    position: absolute; left: 30px; top: 384px;
    font-family: "Michroma", sans-serif; font-size: 25px; letter-spacing: 1px;
    color: var(--ink);
  }
  .headline-band {
    position: absolute; left: 0; top: 433px; width: 900px; height: 50px;
    background: var(--green);
  }
  .headline-band::before {
    content: ""; position: absolute; left: 0; top: 0; width: 40px; height: 50px;
    background: var(--green-dark);
    clip-path: polygon(0 0, 100% 0, 60% 100%, 0 100%);
  }
  .headline-band span {
    position: absolute; left: 42px; top: 12px;
    font-family: "Michroma", sans-serif; font-size: 23px; letter-spacing: 1px;
    color: var(--ink);
  }
  .brand-mark {
    position: absolute; left: 655px; top: 350px; width: 150px; height: 150px;
    border-radius: 50%; background: var(--ink);
  }
  .about-panel {
    position: absolute; left: 540px; top: 483px; width: 360px; height: 475px;
    background: var(--panel);
  }
  .brand-name {
    position: absolute; left: 560px; top: 546px; width: 320px; text-align: center;
    font-weight: 900; font-size: 48px; color: var(--green); letter-spacing: 1px;
  }
  .brand-tagline {
    position: absolute; left: 560px; top: 604px; width: 320px; text-align: center;
    font-size: 19px; letter-spacing: 3px; color: var(--muted);
  }
  .about-text {
    position: absolute; left: 560px; top: 660px; width: 310px;
    font-size: 17.5px; line-height: 23px; text-align: justify; color: var(--text);
  }
  .advantage {
    position: absolute; width: 150px; text-align: center;
  }
  .advantage svg { display: block; margin: 0 auto; }
  .advantage p {
    font-size: 17px; line-height: 19px; color: var(--text); margin-top: 2px;
  }
  .section-band {
    position: absolute; left: 0; top: 939px; width: 455px; height: 40px;
    background: var(--green);
    clip-path: polygon(0 0, 100% 0, 94% 100%, 0 100%);
  }
  .section-band span {
    position: absolute; left: 48px; top: 7px;
    font-family: "Michroma", sans-serif; font-size: 19px; letter-spacing: 1px; color: var(--ink);
  }
  .section-text {
    position: absolute; left: 50px; top: 992px; width: 832px;
    font-size: 17.5px; line-height: 24.5px; text-align: justify;
  }
  .footer-black {
    position: absolute; left: 0; top: 1127px; width: 900px; height: 73px;
    background: var(--black);
    clip-path: polygon(0 0, 555px 0, 540px 26px, 900px 26px, 900px 100%, 0 100%);
  }
  .footer-green {
    position: absolute; left: 441px; top: 1153px; width: 459px; height: 47px;
    background: var(--green);
    clip-path: polygon(28px 0, 100% 0, 100% 100%, 0 100%);
  }
  .phone {
    position: absolute; left: 52px; top: 1163px;
    font-weight: 700; font-size: 25px; color: var(--white); letter-spacing: 0.5px;
  }
  .website {
    position: absolute; left: 500px; top: 1162px; width: 390px; text-align: center;
    font-size: 25px; letter-spacing: 5px; color: var(--ink);
  }
</style>
</head>
<body>
<main class="flyer">
  <div class="hero-photo" role="img" aria-label="Photo of two electric outboard motors on the stern of a boat with white wake water between them"></div>

  <h1 class="headline">REBUILD EVERY BOAT INTO AN</h1>
  <div class="headline-band"><span>ELECTRICALLY PROPELLED BOAT</span></div>

  <div class="about-panel"></div>
  <div class="brand-mark"></div>
  <div class="brand-name">VOLTA KADE</div>
  <div class="brand-tagline">ELEKTRISCH VAREN</div>
  <p class="about-text">Volta Kade is a shipyard in Amsterdam with one of its core activities being the conversion of existing, traditionally powered, boats to electric propulsion. There is a great ambition here and this is also in line with the intention of the municipality of Amsterdam to allow all movement on the water to take place emission-free from 2025.</p>

  <!-- advantages row 1 -->
  <div class="advantage" style="left:14px; top:509px;">
    <svg width="110" height="122" viewBox="0 0 110 122">
      <path d="M17 50 A38 38 0 1 1 55 88 L55 120" fill="none" stroke="var(--green)" stroke-width="2.5"/>
      <circle cx="55" cy="50" r="29" fill="var(--ink)"/>
      <path d="M44 45 h6 l8-7 v24 l-8-7 h-6z" fill="none" stroke="#fff" stroke-width="2"/>
      <line x1="42" y1="36" x2="68" y2="64" stroke="#fff" stroke-width="2"/>
    </svg>
    <p>completely<br>silent</p>
  </div>
  <div class="advantage" style="left:136px; top:509px;">
    <svg width="110" height="122" viewBox="0 0 110 122">
      <path d="M17 50 A38 38 0 1 1 55 88 L55 114" fill="none" stroke="var(--green)" stroke-width="2.5"/>
      <path d="M50 112 L55 120 L60 112z" fill="var(--green)"/>
      <circle cx="55" cy="50" r="29" fill="#fff" stroke="var(--ink)" stroke-width="2"/>
      <rect x="44" y="34" width="22" height="28" rx="2" fill="none" stroke="var(--ink)" stroke-width="2"/>
      <text x="55" y="56" text-anchor="middle" font-family="Lato, sans-serif" font-weight="700" font-size="16" fill="var(--ink)">$</text>
    </svg>
    <p>cheap to<br>operate</p>
  </div>
  <div class="advantage" style="left:245px; top:509px;">
    <svg width="110" height="122" viewBox="0 0 110 122">
      <path d="M17 50 A38 38 0 1 1 55 88 L55 120" fill="none" stroke="var(--green)" stroke-width="2.5"/>
      <circle cx="55" cy="50" r="29" fill="var(--ink)"/>
      <line x1="42" y1="37" x2="68" y2="63" stroke="#fff" stroke-width="3"/>
      <line x1="68" y1="37" x2="42" y2="63" stroke="#fff" stroke-width="3"/>
      <circle cx="42" cy="37" r="4" fill="none" stroke="#fff" stroke-width="2"/>
    </svg>
    <p>no<br>maintenance</p>
  </div>
  <div class="advantage" style="left:347px; top:509px;">
    <svg width="110" height="122" viewBox="0 0 110 122">
      <path d="M17 50 A38 38 0 1 1 55 88 L55 114" fill="none" stroke="var(--green)" stroke-width="2.5"/>
      <path d="M50 112 L55 120 L60 112z" fill="var(--green)"/>
      <circle cx="55" cy="50" r="29" fill="#fff" stroke="var(--ink)" stroke-width="2"/>
      <path d="M42 48 h6 v14 h-6z M48 49 l6-12 c3 0 4 2 3 6 l-1 4 h9 c2 0 3 2 2 4 l-3 9 c-1 2-2 2-4 2 h-12z" fill="none" stroke="var(--ink)" stroke-width="2" stroke-linejoin="round"/>
    </svg>
    <p>more<br>enjoyable</p>
  </div>

  <!-- advantages row 2 -->
  <div class="advantage" style="left:33px; top:712px;">
    <svg width="110" height="122" viewBox="0 0 110 122">
      <path d="M17 50 A38 38 0 1 1 55 88 L55 120" fill="none" stroke="var(--green)" stroke-width="2.5"/>
      <circle cx="55" cy="50" r="29" fill="var(--ink)"/>
      <circle cx="55" cy="50" r="15" fill="none" stroke="#fff" stroke-width="2"/>
      <rect x="44" y="48" width="22" height="5" fill="#fff"/>
      <line x1="45" y1="40" x2="65" y2="60" stroke="#fff" stroke-width="2"/>
    </svg>
    <p>no fumes, smells<br>or smoke</p>
  </div>
  <div class="advantage" style="left:185px; top:712px;">
    <svg width="110" height="122" viewBox="0 0 110 122">
      <path d="M17 50 A38 38 0 1 1 55 88 L55 114" fill="none" stroke="var(--green)" stroke-width="2.5"/>
      <path d="M50 112 L55 120 L60 112z" fill="var(--green)"/>
      <circle cx="55" cy="50" r="29" fill="#fff" stroke="var(--ink)" stroke-width="2"/>
      <path d="M55 33 a9 9 0 0 1 5 16 v6 h-10 v-6 a9 9 0 0 1 5-16z" fill="none" stroke="var(--ink)" stroke-width="2"/>
      <line x1="50" y1="59" x2="60" y2="59" stroke="var(--ink)" stroke-width="2"/>
      <line x1="52" y1="63" x2="58" y2="63" stroke="var(--ink)" stroke-width="2"/>
    </svg>
    <p>obliged in more<br>and more areas</p>
  </div>
  <div class="advantage" style="left:334px; top:712px;">
    <svg width="110" height="122" viewBox="0 0 110 122">
      <path d="M17 50 A38 38 0 1 1 55 88 L55 120" fill="none" stroke="var(--green)" stroke-width="2.5"/>
      <circle cx="55" cy="50" r="29" fill="var(--ink)"/>
      <circle cx="55" cy="48" r="13" fill="none" stroke="#fff" stroke-width="2"/>
      <ellipse cx="55" cy="48" rx="6" ry="13" fill="none" stroke="#fff" stroke-width="1.5"/>
      <line x1="42" y1="48" x2="68" y2="48" stroke="#fff" stroke-width="1.5"/>
      <path d="M40 62 q15 8 30 0" fill="none" stroke="#fff" stroke-width="2"/>
    </svg>
    <p>environmentally<br>friendly</p>
  </div>

  <div class="section-band"><span>BEST SUITABLE SOLUTION</span></div>
  <p class="section-text">Volta Kade is a shipyard in Amsterdam with one of its core activities being the conversion of existing, traditionally powered, boats to electric propulsion. There is a great ambition here and this is also in line with the intention of the municipality of Amsterdam to allow all movement on the water to take place emission-free from 2025.</p>

  <div class="footer-black"></div>
  <div class="footer-green"></div>
  <div class="phone">CALL US-+31 6 12 345 678</div>
  <div class="website">www.volta-kade.nl</div>
</main>
</body>
</html>
```